Business Card design for construction company

I would like a business card design for a construction company - Harlow Constructions. I have attached the ai logo file for use. I would like the card to be very smart and clean and incorporate only white and the two colours in the logo. I would like the card to have two sides. One side can just have the logo, the other with the relevant information.

Target Market(s)

Building and Construction Clients

Industry/Entity Type

Business

Contact Information for Business Card

Name: Tom Pardoe
Company: Harlow Constructions Pty Limited
Address: 14 Mallee Crescent Carrow Vale 2093
Phone: 0427 531 068
Email: tomp@harlowbuild-example.com.au

Font styles to use
Serif
Sans Serif

Requirements
Must have
• Details noted above
• Logo as provided
• Colours as in logo
• Square edges
• A font that compliments the logo
Should not have
• Any colour other than white and those in logo
• Rounded edges

```html
<!DOCTYPE html>
<html lang="en">
<head>
<meta charset="utf-8">
<title>Harlow Constructions – Business Card</title>
<link rel="stylesheet" href="https://fonts.googleapis.com/css2?family=Jost:wght@300;400&display=swap">
<style>
  :root {
    --ink-grey: #58595b;
    --accent-blue: #1ba9e6;
    --paper: #ffffff;
  }
  html, body {
    margin: 0;
    padding: 0;
    overflow: hidden;
    background: var(--paper);
  }
  .card {
    position: relative;
    width: 1200px;
    height: 742px;
    background: var(--paper);
    color: var(--ink-grey);
    font-family: "Jost", sans-serif;
    font-weight: 300;
    overflow: hidden;
  }
  .brand-name {
    position: absolute;
    left: 4px;
    top: 58px;
    margin: 0;
    font-size: 66px;
    font-weight: 300;
    line-height: 1;
    letter-spacing: 7px;
    text-transform: uppercase;
    color: var(--ink-grey);
    white-space: nowrap;
  }
  .legal-name {
    position: absolute;
    left: 381px;
    top: 160px;
    margin: 0;
    font-size: 42px;
    line-height: 1;
    letter-spacing: 2px;
    white-space: nowrap;
  }
  .person-name {
    position: absolute;
    left: 2px;
    top: 318px;
    margin: 0;
    font-size: 56px;
    line-height: 1;
    white-space: nowrap;
  }
  .icon {
    position: absolute;
    fill: var(--accent-blue);
  }
  .icon-pin { left: 530px; top: 325px; width: 68px; height: 94px; }
  .icon-phone { left: 527px; top: 505px; width: 74px; height: 64px; }
  .address {
    position: absolute;
    left: 624px;
    top: 310px;
    margin: 0;
    font-size: 48px;
    font-style: normal;
    line-height: 62px;
    white-space: nowrap;
  }
  .phone {
    position: absolute;
    left: 624px;
    top: 506px;
    margin: 0;
    font-size: 48px;
    line-height: 62px;
    letter-spacing: 1px;
    white-space: nowrap;
  }
  .divider {
    position: absolute;
    left: 210px;
    top: 640px;
    width: 764px;
    height: 8px;
    background: var(--ink-grey);
  }
  .email {
    position: absolute;
    left: 0;
    width: 1180px;
    top: 684px;
    margin: 0;
    font-size: 46px;
    line-height: 1;
    text-align: center;
    white-space: nowrap;
  }
</style>
</head>
<body>
  <main class="card">
    <h1 class="brand-name">Harlow Constructions</h1>
    <p class="legal-name">Harlow Constructions Pty Limited</p>

    <p class="person-name">Tom Pardoe</p>

    <svg class="icon icon-pin" viewBox="0 0 68 94" aria-hidden="true">
      <path d="M34 0C15.2 0 0 15.2 0 34c0 22 34 60 34 60s34-38 34-60C68 15.2 52.8 0 34 0zm0 48a14 14 0 1 1 0-28 14 14 0 0 1 0 28z"/>
    </svg>
    <address class="address">14 Mallee Crescent<br>Carrow Vale 2093</address>

    <svg class="icon icon-phone" viewBox="0 0 74 64" aria-hidden="true">
      <path d="M4 20C4 8 20 2 37 2s33 6 33 18v4H54v-6c0-3-8-5-17-5s-17 2-17 5v6H4z"/>
      <path d="M20 22h34l14 18v18c0 3-2 5-5 5H11c-3 0-5-2-5-5V40z"/>
      <g fill="#ffffff">
        <rect x="24" y="32" width="7" height="6"/><rect x="34" y="32" width="7" height="6"/><rect x="44" y="32" width="7" height="6"/>
        <rect x="24" y="41" width="7" height="6"/><rect x="34" y="41" width="7" height="6"/><rect x="44" y="41" width="7" height="6"/>
        <rect x="24" y="50" width="7" height="6"/><rect x="34" y="50" width="7" height="6"/><rect x="44" y="50" width="7" height="6"/>
      </g>
    </svg>
    <p class="phone">042.753.1068</p>

    <div class="divider"></div>
    <p class="email">tomp@harlowbuild-example.com.au</p>
  </main>
</body>
</html>
```